A new medical waste company needs an attractive and modern flyer.

We are a new medical waste company disposing of biohazards waste, red bag waste and sharps disposal with a focus on customer service.

Background Information

Company Name
Trovik Waste

Industry
Medical waste management

Description of the organization and its target audience

We are a new medical waste company disposing of biohazardous waste, red bag waste and medical sharps.

Description

MODERN & ELEGANT HALF PAGE FLYER

Half page mailer (front and back) with a large image related to the medical field.

The Trovik Waste logo, with the company tag line “compliant waste solutions” should also be on front of the mailer.

Website (trovikwaste.com) & email (info@trovikwatse.com) on both sides of the flyer

Main headline
-Now you have options for your medical waste disposal

Who we serve
- Dentist
- Physicians
-Blood banks
-Tattoo parlors
-Assisted living facilities
-Laboratories
-Veterinarians

What we offer
-Straight forward pricing
-No hidden fees
-No long term contracts
-Free containers and red bags
-Routine scheduled pickups

Price $35.95
Updates

Remember this is a half page flyer. Please remove pricing from all future work.

Target Market(s)

- Dentist
- Physicians
-Blood banks
-Tattoo parlors
-Laboratories
-Veterinarians

Industry/Entity Type

It Company

Colors
33b8a4

Requirements
Must have
• See my website www.trovikwaste.com

```html
<!DOCTYPE html>
<html lang="en">
<head>
<meta charset="utf-8">
<title>Trovik Waste – Half Page Flyer</title>
<link rel="stylesheet" href="https://fonts.googleapis.com/css2?family=Lato:wght@300;400;700;900&display=swap">
<style>
  :root {
    --teal: #33b8a4;
    --teal-deep: #2aa592;
    --ink: #1d1f22;
    --white: #ffffff;
    --page: #e6e7e8;
    --photo-a: #c9d3d2;
    --photo-b: #6f8f98;
    --photo-c: #3d6f8f;
    --ring: #d8e6e4;
  }
  * { box-sizing: border-box; margin: 0; padding: 0; }
  html, body {
    width: 1200px; height: 800px; overflow: hidden;
    background: var(--page);
    font-family: "Lato", sans-serif;
  }
  .flyer {
    position: absolute; left: 50px; top: 25px;
    width: 1100px; height: 750px;
    overflow: hidden;
    box-shadow: 0 14px 34px rgba(0,0,0,.25);
  }
  .flyer__photo {
    position: absolute; inset: 0;
    background:
      radial-gradient(ellipse at 38% 40%, #e7d6cc 0%, rgba(231,214,204,0) 28%),
      radial-gradient(ellipse at 22% 62%, var(--photo-c) 0%, rgba(61,111,143,0) 30%),
      linear-gradient(120deg, var(--photo-a) 0%, var(--photo-b) 55%, #a9bcbc 100%);
  }
  .flyer__panel { position: absolute; inset: 0; }
  .price-badge {
    position: absolute; left: 62px; top: 72px;
    width: 180px; height: 180px; border-radius: 50%;
    background: var(--teal);
    border: 9px solid var(--ring);
    color: var(--white);
    display: flex; flex-direction: column; align-items: center; justify-content: center;
  }
  .price-badge__label { font-weight: 400; font-size: 29px; line-height: 1.1; }
  .price-badge__amount { font-weight: 700; font-size: 38px; line-height: 1.2; }
  .contact {
    position: absolute; left: 30px; bottom: 38px;
    display: flex; gap: 46px;
    font-weight: 700; font-size: 23px; color: var(--ink);
  }
  .brand {
    position: absolute; right: 46px; top: 52px;
    display: flex; align-items: center; gap: 16px;
  }
  .brand__mark {
    width: 52px; height: 52px; border-radius: 50%;
    border: 3px solid var(--ink);
  }
  .brand__name {
    font-weight: 700; font-size: 30px; letter-spacing: 1px;
    color: var(--ink); text-transform: uppercase;
  }
  .info {
    position: absolute; left: 650px; top: 185px;
    color: var(--white);
  }
  .info__heading {
    font-size: 33px; font-weight: 300;
    border-left: 4px solid var(--white);
    padding-left: 8px; line-height: 1;
    margin-bottom: 14px;
  }
  .info__heading strong { font-weight: 700; }
  .info__list { list-style: none; margin-bottom: 32px; }
  .info__list li {
    font-size: 20px; font-weight: 400; line-height: 29px;
    padding-left: 14px; position: relative;
  }
  .info__list li::before {
    content: "›"; position: absolute; left: 0; top: -1px;
    font-weight: 900; font-size: 22px;
  }
</style>
</head>
<body>
  <article class="flyer">
    <div class="flyer__photo" role="img" aria-label="Photo of a lab technician in a white coat and blue gloves working with sample tubes"></div>

    <svg class="flyer__panel" width="1100" height="750" viewBox="0 0 1100 750" aria-hidden="true">
      <polygon points="690,0 1100,0 1100,750 660,750 392,378" fill="var(--teal)"/>
      <polygon points="432,378 486,312 486,444" fill="var(--ink)"/>
    </svg>

    <div class="price-badge">
      <span class="price-badge__label">Price</span>
      <span class="price-badge__amount">$35.95</span>
    </div>

    <div class="brand">
      <span class="brand__mark"></span>
      <span class="brand__name">Trovik Waste</span>
    </div>

    <section class="info">
      <h2 class="info__heading">Who We <strong>Serve</strong></h2>
      <ul class="info__list">
        <li>Dentist</li>
        <li>Physicians</li>
        <li>Blood banks</li>
        <li>Tattoo parlors</li>
        <li>Assisted living facilities</li>
        <li>Laboratories</li>
        <li>Veterinarians</li>
      </ul>
      <h2 class="info__heading">What We <strong>Offer</strong></h2>
      <ul class="info__list">
        <li>Straight forward pricing</li>
        <li>No hidden fees</li>
        <li>No long term contracts</li>
        <li>Free containers and red bags</li>
        <li>Routine scheduled pickups</li>
      </ul>
    </section>

    <div class="contact">
      <span class="contact__web">www.trovikwaste.com</span>
      <span class="contact__mail">info@trovikwatse.com</span>
    </div>
  </article>
</body>
</html>
```